Upmarket Bathroom and Kitchen ware supplier needs a classy business card design

We are a company based in Fiji, we sell plumbing ware (Kitchen and bathroom taps, Basins,showers, toilets etc) through up market show rooms to individuals and directly through Architects and designers of resorts and holiday houses for new builds and renovations. we are wanting to upgrade our over all look and brand. we are starting with a new logo but will be rebranding the whole business. This project is for a business card design for my management and tales team I would like it to be dark, classy and interesting

Target Market(s)

Resort directors and Management, High end holiday home owners

Contact Information for Business Card

Neil Dawson
Director
+64219473815

Colors

Designer to choose colors to be used in the design.

Requirements
Must have
• Must have an upmarket appearance I like darker charcoal shades but will be guided by the designers
• Please any catch phrases like "Crafting remarkable living rooms" this belongs tpo one of our suppliers so can not be used.
Nice to have
• Double sided, so front dedicated to logo provided and back info about the business and the person.

```html
<!DOCTYPE html>
<html lang="en">
<head>
<meta charset="utf-8">
<title>Lagoon Fixtures — Business Card</title>
<link rel="stylesheet" href="https://fonts.googleapis.com/css2?family=Montserrat:wght@300;400;700&display=swap">
<style>
  :root {
    --backdrop: #e6e6e6;
    --card: #303032;
    --accent-ring: #3c3c3f;
    --ink-light: #e4e4e6;
    --ink-muted: #8e8e92;
    --ink-soft: #a9a9ad;
  }
  * { margin: 0; padding: 0; box-sizing: border-box; }
  html, body {
    width: 1200px;
    height: 900px;
    overflow: hidden;
    background: var(--backdrop);
    font-family: "Montserrat", sans-serif;
  }
  .sheet {
    position: relative;
    width: 1200px;
    height: 900px;
  }
  .card {
    position: absolute;
    width: 490px;
    height: 280px;
    background: var(--card);
    box-shadow: 0 14px 30px rgba(0, 0, 0, 0.18);
    overflow: hidden;
  }
  .card--front { left: 90px; top: 430px; }
  .card--back { left: 620px; top: 190px; }

  .card__ring {
    position: absolute;
    inset: 0;
    width: 100%;
    height: 100%;
  }
  .card__ring circle {
    fill: none;
    stroke: var(--accent-ring);
    stroke-width: 14;
  }

  .brand {
    position: absolute;
    left: 50px;
    top: 150px;
    display: flex;
    align-items: center;
    gap: 14px;
  }
  .brand__dot {
    width: 12px;
    height: 12px;
    border-radius: 50%;
    background: var(--ink-muted);
  }
  .brand__name {
    font-weight: 300;
    font-size: 22px;
    letter-spacing: 0.32em;
    text-transform: uppercase;
    color: var(--ink-muted);
  }

  .contact {
    position: absolute;
    left: 40px;
    top: 36px;
  }
  .contact__name {
    font-weight: 700;
    font-size: 21px;
    letter-spacing: 0.02em;
    text-transform: uppercase;
    color: var(--ink-light);
  }
  .contact__line {
    margin-top: 6px;
    font-weight: 400;
    font-size: 11.5px;
    letter-spacing: 0.04em;
    text-transform: uppercase;
    color: var(--ink-soft);
  }
  .contact__sep { margin: 0 4px; }
</style>
</head>
<body>
  <main class="sheet">
    <section class="card card--front" aria-label="Card front">
      <svg class="card__ring" viewBox="0 0 490 280" aria-hidden="true">
        <circle cx="470" cy="60" r="170"/>
      </svg>
      <div class="brand">
        <span class="brand__dot"></span>
        <span class="brand__name">Lagoon Fixtures</span>
      </div>
    </section>

    <section class="card card--back" aria-label="Card back">
      <svg class="card__ring" viewBox="0 0 490 280" aria-hidden="true">
        <circle cx="420" cy="290" r="170"/>
      </svg>
      <div class="contact">
        <p class="contact__name">Neil Dawson</p>
        <p class="contact__line">Director<span class="contact__sep">•</span>+64219473815</p>
      </div>
    </section>
  </main>
</body>
</html>
```